依頼詳細
封筒2種類(角2・長3)のデザインをお願いします。
会社のロゴは決まったものがあります。
名刺デザインを踏襲したようなデザインが希望です。
記載項目
添付する名刺同様に、名刺の表の内容を表に、裏の内容を裏にお願いします
表は4Cで結構ですが、裏は1Cでお願いします。
希望イメージ
シンプル 複雑
単色 カラフル
暗い 明るい
日常 高級
遊び心 厳粛
未来的 伝統的
女性的 男性的
希望する色
青系、ベースは白でブルー系でお願いします。
納品ファイル
• イラストレーター形式 (.ai)
補足説明
ロゴは仕様書がありますので添付します。
名刺のデザインを添付します。
■ 選んだ理由

この度はご提案・ご修正等、スムーズにご対応いただきまして誠にありがとうございます。検討したました結果、tokirenaさんにお願いすることにいたしました。23件ご提案をいただきまして、皆さんキレイなデザインで大きな違いはなく、非常に迷いましたが、数案バリエーションでご提案いただき、レスポンスが良かった点が決めてでした。

■ 提案者全員のお礼・コメント

この度はご提案・ご修正等、スムーズにご対応いただきまして誠にありがとうございます。23件ご提案をいただきまして、皆さんキレイなデザインで大きな違いはなく、非常に迷いましたが、数案バリエーションでご提案いただき、レスポンスが良かった点が決めてでした。

```html
<!DOCTYPE html>
<html lang="ja">
<head>
<meta charset="utf-8">
<title>角2封筒 表 — 株式会社ノードウェル</title>
<link rel="stylesheet" href="https://fonts.googleapis.com/css2?family=Noto+Sans+JP:wght@400;500;700;900&display=swap">
<style>
  :root {
    --page: #ffffff;
    --paper: #ffffff;
    --edge: #b9bcc0;
    --ink: #4a4d52;
    --ink-soft: #8a8d92;
    --brand: #2f6fba;
    --band-start: #1d4f9c;
    --band-end: #3fa0dc;
    --ghost: #f3f4f6;
  }
  * { margin: 0; padding: 0; box-sizing: border-box; }
  html, body { width: 784px; height: 1200px; overflow: hidden; background: var(--page); }
  body { position: relative; font-family: "Noto Sans JP", sans-serif; color: var(--ink); }

  .sheet-label {
    position: absolute; left: 30px; top: 26px;
    font-size: 13px; color: var(--ink);
  }

  .envelope {
    position: absolute; left: 46px; top: 64px;
    width: 692px; height: 1122px;
    background: var(--paper);
    border: 1.5px solid var(--edge);
    overflow: hidden;
  }
  .flap-line {
    position: absolute; left: 0; right: 0; top: 186px;
    border-top: 1.5px solid var(--edge);
  }

  .flap-sender {
    position: absolute; left: 0; right: 0; top: 40px;
    transform: rotate(180deg);
    text-align: center;
  }
  .flap-sender .row { display: flex; justify-content: center; align-items: center; gap: 14px; }
  .flap-sender .name { font-size: 15px; font-weight: 700; color: var(--ink); letter-spacing: 0.04em; }
  .flap-sender .mark { width: 14px; height: 14px; background: var(--brand); }
  .flap-sender .url { font-size: 10px; color: var(--brand); }
  .flap-sender .address { margin-top: 6px; font-size: 9px; color: var(--ink-soft); }

  .ghost-disc {
    position: absolute; left: 410px; top: 770px;
    width: 240px; height: 240px; border-radius: 50%;
    background: var(--ghost);
  }

  .brand-lockup {
    position: absolute; left: 34px; top: 924px;
    display: flex; align-items: center; gap: 12px;
  }
  .brand-lockup .mark { width: 34px; height: 34px; background: var(--brand); }
  .brand-lockup .name { font-size: 46px; font-weight: 900; color: var(--brand); line-height: 1; letter-spacing: -0.01em; }
  .brand-url {
    position: absolute; left: 310px; top: 946px;
    font-size: 15px; color: var(--brand); letter-spacing: 0.08em;
  }

  .sender-band {
    position: absolute; left: 30px; right: 30px; top: 988px; height: 46px;
    background: linear-gradient(90deg, var(--band-start), var(--band-end));
    display: flex; align-items: center; padding: 0 0 0 64px; gap: 32px;
    color: #ffffff;
  }
  .sender-band .company { font-size: 15px; font-weight: 700; letter-spacing: 0.06em; white-space: nowrap; }
  .sender-band .address { font-size: 10px; letter-spacing: 0.02em; white-space: nowrap; }
</style>
</head>
<body>
  <div class="sheet-label">角２封筒 表</div>

  <div class="envelope">
    <div class="flap-sender">
      <div class="row">
        <span class="url">http://www.nordwell.jp</span>
        <span class="mark"></span>
        <span class="name">NORDWELL INC.</span>
      </div>
      <div class="address">Nordwell Bldg 4F, 3-5-12 Sakae, Naka-ku, Nagoya 460-0008, Japan</div>
    </div>
    <div class="flap-line"></div>

    <div class="ghost-disc" aria-hidden="true"></div>

    <div class="brand-lockup">
      <span class="mark"></span>
      <span class="name">Nordwell</span>
    </div>
    <div class="brand-url">http://www.nordwell.jp</div>

    <div class="sender-band">
      <span class="company">株式会社ノードウェル</span>
      <span class="address">〒460-0008 愛知県名古屋市中区栄3-5-12 ノードウェルビル4F TEL 052-000-0000</span>
    </div>
  </div>
</body>
</html>
```